Bright Canvas Guild

wall art that with words that inspire and can uplift people in their homes in times when they are down. An ever present presence to inspire that the subconscious takes in and subliminally feeds the home owner with positivity. Quotes... 1)In the morning, devour the prey, in the evening, divide the spoils. 2)Your situation is not your potential, but your potential depends on how you see your situation. 3)It is never too late, if your still here, then there is still time. 4)Busy your mind with the concepts of harmony, health, peace, and good will, and wonders will happen in your life. 5), it is hard to think straight while going around in circles. 6)you have everything you need to proceed. thses are just a few examples.
I would like to have colourful backgrounds. I am starting a online poster store and need a series of beautifully designed words and colours or pictures that go together like a song and it's two elements of words and music.

Target Market(s)

Anybody with a wall that wants an uplifting presence

Industry/Entity Type

Wall art, home decor

Font styles to use
Serif
Other font styles liked:
• stencil, Dead kansas, newspaper headline styles

Requirements
Must have
• I got to put that on my wall, it's amazing
Nice to have
• I am a martial artist, music producer, writer, lyricist that likes to inspire, and I also appreciate nature and beauty, how this can be incorporated into an artistic expression would be ideal elements. maybe also the colours of

```html
<!DOCTYPE html>
<html lang="en">
<head>
<meta charset="utf-8">
<title>It Is Never Too Late – Bright Canvas Guild</title>
<link rel="stylesheet" href="https://fonts.googleapis.com/css2?family=Bebas+Neue&display=swap">
<style>
  :root {
    --bg: #2b2b2b;
    --red: #e41f26;
    --white: #e6e5ea;
  }
  html, body {
    margin: 0;
    padding: 0;
    width: 848px;
    height: 1200px;
    overflow: hidden;
    background: var(--bg);
  }
  .poster {
    display: block;
    width: 848px;
    height: 1200px;
  }
  .poster text {
    font-family: "Bebas Neue", "Oswald", sans-serif;
  }
  .accent { fill: var(--red); }
  .plain { fill: var(--white); }
</style>
</head>
<body>
<svg class="poster" viewBox="0 0 848 1200" xmlns="http://www.w3.org/2000/svg" role="img"
     aria-label="It is never too late if you are still here, then there is still time">
  <rect class="backdrop" width="848" height="1200" fill="var(--bg)"/>

  <!-- line 1 -->
  <text class="plain side-word" transform="translate(210,300) rotate(-90)" font-size="150"
        textLength="170" lengthAdjust="spacingAndGlyphs">IT IS</text>
  <text class="accent" x="215" y="298" font-size="240"
        textLength="490" lengthAdjust="spacingAndGlyphs">NEVER</text>

  <!-- line 2 -->
  <text class="accent" x="105" y="470" font-size="221"
        textLength="260" lengthAdjust="spacingAndGlyphs">TOO</text>
  <text class="plain" x="372" y="470" font-size="221"
        textLength="333" lengthAdjust="spacingAndGlyphs">LATE</text>

  <!-- line 3 -->
  <text class="plain" x="105" y="615" font-size="186"
        textLength="355" lengthAdjust="spacingAndGlyphs">IF YOU</text>
  <text class="accent" x="476" y="615" font-size="186"
        textLength="229" lengthAdjust="spacingAndGlyphs">ARE</text>

  <!-- line 4 -->
  <text class="accent side-word" transform="translate(205,850) rotate(-90)" font-size="143"
        textLength="220" lengthAdjust="spacingAndGlyphs">STILL</text>
  <text class="plain" x="212" y="850" font-size="314"
        textLength="493" lengthAdjust="spacingAndGlyphs">HERE</text>
  <path class="accent comma" d="M712 815 H748 L734 880 H716 L726 850 H712 Z"/>

  <!-- line 5 -->
  <text class="plain" x="105" y="924" font-size="79"
        textLength="120" lengthAdjust="spacingAndGlyphs">THEN</text>
  <text class="accent" x="232" y="924" font-size="79"
        textLength="146" lengthAdjust="spacingAndGlyphs">THERE</text>
  <text class="plain" x="388" y="924" font-size="79"
        textLength="50" lengthAdjust="spacingAndGlyphs">IS</text>
  <g class="accent rule-bars">
    <rect x="450" y="872" width="255" height="10"/>
    <rect x="450" y="893" width="255" height="10"/>
    <rect x="450" y="914" width="255" height="10"/>
  </g>

  <!-- line 6 -->
  <text class="accent" x="105" y="1070" font-size="186"
        textLength="310" lengthAdjust="spacingAndGlyphs">STILL</text>
  <text class="plain" x="430" y="1070" font-size="186"
        textLength="275" lengthAdjust="spacingAndGlyphs">TIME</text>
</svg>
</body>
</html>
```